Email Marketing for Post-wren

I am a sports photographer and I would like to have an email distribution that I can send out after an event or have something go out on a more regular basis.

juniperridge-peakshot.com

I can supply the looks and so on I am looking for a template that I can reuse time and time again.

I want something that works with Postwren.

http://postwrenmail.com

It must conform to there templates and I would like to be able to put some photo's in the template as well.

Target Market(s)

Parents and Families attending events and wishing to purchase photos from that day.

Industry/Entity Type

Marketing

Font styles to use
Serif

Requirements
Must have
• Must have my logo.
• Must use the same font museo 500.
• Must be Red, Grey and White same as the logo.
• Must have Facebook links https://www.pallorium.net/JuniperRidgePeakshot
• Must have twitter links @junipeakshot
• Must have email address info@juniperridge-peakshot.com
• Must have room for other company logo's in the future
• Should be broken down in sections

```html
<!DOCTYPE html>
<html lang="en">
<head>
<meta charset="utf-8">
<title>Juniperridge Peakshot – Newsletter</title>
<link href="https://fonts.googleapis.com/css2?family=Open+Sans:ital,wght@0,400;0,600;0,700;1,400&display=swap" rel="stylesheet">
<style>
  :root {
    --red: #e3222b;
    --grey-text: #6d6d6d;
    --grey-dark: #3a3a3a;
    --panel: #ececec;
    --white: #ffffff;
    --line: #d7d7d7;
  }
  * { box-sizing: border-box; margin: 0; padding: 0; }
  html, body { width: 764px; height: 1200px; overflow: hidden; background: var(--white); }
  body { font-family: "Open Sans", Arial, sans-serif; color: var(--grey-text); position: relative; }

  .top-bar { position: absolute; top: 0; left: 0; width: 764px; height: 34px; }
  .top-bar__rule { position: absolute; top: 0; left: 0; width: 540px; height: 6px; background: var(--red); }
  .top-bar__date { position: absolute; top: 0; right: 0; width: 214px; height: 34px; background: var(--red);
    color: var(--white); font-size: 16px; font-weight: 600; display: flex; align-items: center; justify-content: center; }
  .top-bar__date sup { font-size: 10px; }

  .brand { position: absolute; top: 52px; left: 0; width: 764px; text-align: center; }
  .brand__mark { display: inline-block; width: 22px; height: 22px; background: var(--red); margin-bottom: 10px; }
  .brand__name { font-size: 38px; font-weight: 700; color: var(--red); letter-spacing: 1px; line-height: 1.1; }
  .brand__url { font-size: 15px; color: var(--grey-text); margin-top: 8px; }

  .photo { position: absolute; }
  .photo--beach { top: 218px; left: 10px; width: 362px; height: 338px;
    background: linear-gradient(180deg, #7fb3de 0%, #bcd9ee 45%, #3d8fb8 72%, #c7b48e 100%); }
  .photo--pool { top: 218px; left: 390px; width: 364px; height: 338px;
    background: linear-gradient(180deg, #1d64b8 0%, #4f95da 45%, #e9ecef 62%, #19a4c9 100%); }
  .photo--city { top: 792px; left: 0; width: 440px; height: 300px;
    background: linear-gradient(180deg, #6fa6d2 0%, #a9c9e3 28%, #5b6d80 55%, #2f3e4e 100%); }

  .intro { position: absolute; top: 578px; left: 24px; width: 716px; }
  .intro__lead { color: var(--red); font-style: italic; font-size: 17px; }
  .intro__body { margin-top: 18px; font-size: 16px; line-height: 1.45; color: var(--grey-text); }

  .section-head { position: absolute; top: 712px; left: 24px; width: 410px; }
  .section-head__kicker { color: var(--red); font-size: 28px; font-weight: 400; line-height: 1.15; }
  .section-head__title { color: var(--red); font-size: 30px; font-weight: 700; line-height: 1.15; }

  .contact { position: absolute; top: 720px; left: 440px; width: 324px; height: 372px; background: var(--panel); padding: 22px 24px; }
  .contact__heading { text-align: center; font-weight: 700; font-size: 16px; color: var(--grey-dark); }
  .contact__lines { text-align: center; font-size: 15px; line-height: 1.4; color: var(--grey-dark); }
  .contact__follow { margin-top: 26px; text-align: center; font-weight: 700; font-size: 16px; color: var(--grey-dark); }
  .social { list-style: none; margin-top: 22px; }
  .social__item { display: flex; align-items: center; gap: 14px; font-size: 10.5px; color: var(--grey-dark);
    border-bottom: 1px solid var(--line); padding: 10px 0; }
  .social__item:last-child { border-bottom: none; }
  .social__icon { width: 16px; height: 16px; background: var(--grey-dark); flex: none; }

  .footer-rule { position: absolute; top: 1092px; left: 0; width: 764px; height: 6px; background: var(--red); }
  .partners { position: absolute; top: 1118px; left: 0; width: 764px; height: 64px; display: flex;
    align-items: center; justify-content: center; gap: 26px; }
  .partners__name { font-size: 20px; font-weight: 700; color: var(--grey-dark); }
  .partners__name--client { color: var(--red); }
  .partners__divider { width: 2px; height: 56px; background: var(--grey-dark); }
</style>
</head>
<body>
  <header class="top-bar">
    <div class="top-bar__rule"></div>
    <div class="top-bar__date">July 25<sup>th</sup></div>
  </header>

  <section class="brand">
    <span class="brand__mark"></span>
    <div class="brand__name">JUNIPERRIDGE PEAKSHOT</div>
    <div class="brand__url">www.juniperridge-peakshot.com</div>
  </section>

  <div class="photo photo--beach" role="img" aria-label="Tropical beach with palm trees under a blue sky"></div>
  <div class="photo photo--pool" role="img" aria-label="White umbrellas beside a blue resort pool with palm trees"></div>

  <section class="intro">
    <p class="intro__lead">Lorem Ipsum Dolor Sit Amet, Consectetur Adipiscing.</p>
    <p class="intro__body">Am in aliquam risus. In sit amet dapibus nunc. Cras luctus ipsum eu quam imperdiet faucibus. Vestibulum ex odio, ornare id lectus vitae, vulputate elementum tellus. Pellentesque a felis accumsan, bibendum magna lacinia, rutrum ligula.</p>
  </section>

  <section class="section-head">
    <h2 class="section-head__kicker">POSUERE</h2>
    <h3 class="section-head__title">CONGUE - PROJECTS</h3>
  </section>

  <div class="photo photo--city" role="img" aria-label="City skyline of high-rise towers seen from above"></div>

  <aside class="contact">
    <h4 class="contact__heading">Contac Us:</h4>
    <p class="contact__lines">info@juniperridge-peakshot.com<br>Fernbrook NSW 2071 - Australia<br>Mobile: +61 400 555 013</p>
    <h4 class="contact__follow">Follow On</h4>
    <ul class="social">
      <li class="social__item"><span class="social__icon"></span>https://www.pallorium.net/JuniperRidgePeakshot</li>
      <li class="social__item"><span class="social__icon"></span>@junipeakshot</li>
      <li class="social__item"><span class="social__icon"></span>juniper_peakshot</li>
    </ul>
  </aside>

  <div class="footer-rule"></div>
  <footer class="partners">
    <span class="partners__name">Stowline</span>
    <span class="partners__divider"></span>
    <span class="partners__name partners__name--client">Juniperridge Peakshot</span>
  </footer>
</body>
</html>
```